Letterhead to Prospective Clients

Create a letterhead (word & canva) that I will use to send letters to prospective clients and also include the Coralwood Estate Partners Logo, My Contact Details and Interchangeable "Suburb". Use the same font and colour pallete

Maris Dulworth | "Suburb" Specialist - Redlands & Surrounds
Mobile: 0417 862 095
Email: MD@CoralwoodEstatePartners.com.au

```html
<!DOCTYPE html>
<html lang="en">
<head>
<meta charset="utf-8">
<title>Coralwood Estate Partners Letterhead</title>
<link href="https://fonts.googleapis.com/css2?family=Montserrat:wght@300;400;500;600;700&display=swap" rel="stylesheet">
<style>
  :root {
    --navy: #0f2147;
    --gold: #d6a47a;
    --mist: #f1f2f4;
    --paper: #ffffff;
    --backdrop: #e9e9e9;
  }
  * { margin: 0; padding: 0; box-sizing: border-box; }
  html, body {
    width: 1200px;
    height: 1000px;
    overflow: hidden;
    background: var(--backdrop);
    font-family: "Montserrat", sans-serif;
  }
  .letterhead {
    position: absolute;
    left: 250px;
    top: 19px;
    width: 700px;
    height: 962px;
    background: var(--paper);
  }
  .brand {
    position: absolute;
    top: 64px;
    left: 0;
    right: 0;
    text-align: center;
    color: var(--navy);
    font-weight: 400;
    font-size: 22px;
    letter-spacing: 0.2em;
    text-transform: uppercase;
  }
  .brand-mark {
    position: absolute;
    left: 155px;
    top: 170px;
    width: 390px;
    height: 390px;
    background: var(--mist);
  }
  .footer-rule {
    position: absolute;
    left: 0;
    right: 0;
    top: 846px;
    height: 6px;
    background: var(--gold);
  }
  .footer {
    position: absolute;
    left: 0;
    right: 0;
    top: 852px;
    bottom: 0;
    background: var(--navy);
    text-align: center;
    color: #ffffff;
  }
  .agent-name {
    margin-top: 22px;
    color: var(--gold);
    font-weight: 300;
    font-size: 27px;
    letter-spacing: 0.28em;
    text-transform: uppercase;
    padding-left: 0.28em;
  }
  .agent-title {
    margin-top: 6px;
    font-weight: 600;
    font-size: 7px;
    letter-spacing: 0.42em;
    text-transform: uppercase;
  }
  .agent-contact {
    margin-top: 22px;
    font-weight: 300;
    font-size: 9.5px;
    letter-spacing: 0.02em;
  }
  .agent-contact .label {
    color: var(--gold);
    font-weight: 700;
  }
</style>
</head>
<body>
  <main class="letterhead">
    <header class="brand">Coralwood Estate Partners</header>
    <div class="brand-mark" aria-hidden="true"></div>
    <div class="footer-rule"></div>
    <footer class="footer">
      <div class="agent-name">Maris Dulworth</div>
      <div class="agent-title">Suburb Specialist - Redlands &amp; Surrounds</div>
      <div class="agent-contact">
        <span class="label">M:</span> 0417 862 095 | <span class="label">E:</span> MD@CoralwoodEstatePartners.com.au
      </div>
    </footer>
  </main>
</body>
</html>
```